Modern, Clean, Edgy & Fun Comedy Show Flyer

We need to a create a new flyer for the comedy show, Harbor Laugh Night. The original version of the flyer is attached (file: Old flyer), as well as two versions of the logo.
- The text should be the same except now the show is Every First Wednesday and the next show is June 1.
- Remove the jerk shop logo
- Remove the picture of the man, and replace it with a photo of Delphine (our host), the Audience, or something of your own design.
* pictures of Delphine and the Audience is attached.
* We'd like to keep the same color palette and have also attached a color palette for reference

I have also attached 4 references of flyers that I like, that you can use to get an idea of the theme and aesthetic we are looking for.
* Files: Reference 1, Reference 2, Reference 3, Reference 4
Updates

Colors
3277b5
85acd3
0455a3
eaf1f7
cee9f5
ecf7fb
d5d5d5
e6e6e6

Requirements
Must have
• The harbor laugh night logo attached
• The text as specified in the project description
• An option with Delphine and without

```html
<!DOCTYPE html>
<html lang="en">
<head>
<meta charset="utf-8">
<title>Harbor Laugh Night – Comedy Show Flyer</title>
<link href="https://fonts.googleapis.com/css2?family=Oswald:wght@500;600&family=Righteous&display=swap" rel="stylesheet">
<style>
  :root {
    --ink: #050505;
    --paper: #ffffff;
    --night: #0e2a5c;
    --night-deep: #081a3d;
    --stage-blue: #1c63d8;
    --band-blue: #0f56d9;
    --haze: #3277b5;
    --silver: #d5d5d5;
    --smoke: #6d6d6d;
  }
  * { margin: 0; padding: 0; box-sizing: border-box; }
  html, body { width: 1200px; height: 837px; overflow: hidden; background: #f2f2f2; }
  .flyer {
    position: relative; width: 1200px; height: 837px; overflow: hidden;
    font-family: "Oswald", sans-serif; color: var(--paper);
  }
  .venue-photo {
    position: absolute; left: 0; top: 86px; width: 1200px; height: 751px;
    background:
      radial-gradient(ellipse at 75% 30%, rgba(80,150,255,.55), transparent 55%),
      radial-gradient(ellipse at 15% 45%, rgba(60,130,240,.45), transparent 50%),
      linear-gradient(180deg, var(--stage-blue) 0%, var(--night) 55%, var(--night-deep) 100%);
  }
  .headline {
    position: absolute; left: 0; top: 0; width: 1200px; height: 86px; z-index: 2;
    background: var(--paper); color: var(--ink);
    font-family: "Righteous", sans-serif; font-size: 61px; letter-spacing: 1px;
    text-transform: uppercase; text-align: center; line-height: 90px; white-space: nowrap;
  }
  .headline sup { font-size: 30px; vertical-align: 24px; }
  .host-photo { position: absolute; left: 282px; top: 92px; width: 420px; height: 745px; }
  .featuring-tag {
    position: absolute; left: 0; top: 245px; width: 301px; height: 54px;
    background: var(--band-blue);
    font-family: "Righteous", sans-serif; font-size: 29px; line-height: 54px;
    padding-left: 36px; text-transform: uppercase;
  }
  .lineup { position: absolute; left: 37px; top: 308px; list-style: none; }
  .lineup li { font-size: 32px; font-weight: 500; line-height: 65px; white-space: nowrap; }
  .show-name {
    position: absolute; left: 700px; top: 190px; width: 440px;
    font-size: 62px; font-weight: 600; line-height: 1.08; text-align: center;
    text-transform: uppercase; color: var(--paper);
  }
  .host-band {
    position: absolute; left: 607px; top: 492px; width: 593px; height: 112px;
    background: var(--band-blue); text-align: center;
  }
  .host-band .host { font-size: 40px; font-weight: 600; line-height: 54px; padding-top: 8px; white-space: nowrap; }
  .host-band .date { font-size: 35px; font-weight: 600; line-height: 40px; color: var(--ink); text-transform: uppercase; }
  .details { position: absolute; left: 650px; top: 620px; width: 550px; text-align: center; }
  .details p { font-size: 37px; font-weight: 500; line-height: 54px; white-space: nowrap; }
  .details .divider { color: var(--band-blue); padding: 0 14px; }
</style>
</head>
<body>
<main class="flyer">
  <div class="venue-photo" role="img" aria-label="Blue-toned photo of a bar venue interior with a seated audience"></div>

  <h1 class="headline">Comedy Show Every 1<sup>st</sup> Wednesday</h1>

  <svg class="host-photo" viewBox="0 0 420 745" role="img" aria-label="Black and white cut-out photo of the host holding a microphone on stage">
    <defs>
      <linearGradient id="hostTone" x1="0" y1="0" x2="0" y2="1">
        <stop offset="0" stop-color="#2a2a2a"/>
        <stop offset="0.5" stop-color="#4a4a4a"/>
        <stop offset="1" stop-color="#6d6d6d"/>
      </linearGradient>
    </defs>
    <path d="M70 40 Q80 8 130 6 L300 6 Q345 8 350 50 L360 300 Q410 330 412 400 Q410 440 380 445 L350 440 L340 745 L90 745 L70 450 Q40 420 45 320 Z"
      fill="url(#hostTone)" stroke="#ffffff" stroke-width="8" stroke-linejoin="round"/>
  </svg>

  <div class="featuring-tag">Featuring....</div>
  <ul class="lineup">
    <li>Calvin Rourke,</li>
    <li>Theo Lindqvist,</li>
    <li>Milo Fenwickstein,</li>
    <li>Ravi Dunmore,</li>
    <li>Gemma Okoro</li>
  </ul>

  <p class="show-name">Harbor Laugh Night</p>

  <section class="host-band">
    <p class="host">Hosted by Delphine Marlowe</p>
    <p class="date">Wednesday, June 1st</p>
  </section>

  <section class="details">
    <p>The Tin Lantern</p>
    <p>42 Pier Lane, Harbor Point</p>
    <p>Adm: FREE<span class="divider">|</span>Doors 6:30 PM</p>
  </section>
</main>
</body>
</html>
```